Design for a Note buying company that attracts landlords and seller financed notes

I need a card designed. I want a simple clean front with my logo and contact info. On the back I want some big and bold words to get a message across.

Our Company buys Notes (mortgages) and we want to convey the sense of financial security. Our number one market that we pursue is tired landlords.

If you want to understand our business you can visit our website. www.lakeviewpaperfund.com

Do not use any Clip Art in the design, it will not be accepted. I want a custom designed card not something I could throw together myself. Simple clean and drive the message home.

Target Market(s)

Landlords, seller financed note holders

Industry/Entity Type

Mortgage

Contact Information for Business Card

Simple clean and bold. I need to grab the attention of the customer. It should convey a professional touch.

Font styles to use
Sans Serif

Colors
ec2229
ffffff

Requirements
Must have
• Clean front with logo and contact information
Front colors should match logo

Back should be bold and grab attention. Back colors are open to ideas
Nice to have
• The Back May use the phrase "No more Tentants, No more Toilets" "More Time, More Cash"

I'm open to other ideas about grabbing a landlords attention

I'm open to a square card design
I like cards with round corners as well
Should not have
• any clip art! must be custom designs.

```html
<!DOCTYPE html>
<html lang="en">
<head>
<meta charset="utf-8">
<title>Lakeview Note Buyers – Business Card</title>
<link href="https://fonts.googleapis.com/css2?family=Archivo+Black&family=Montserrat:wght@500;700;800&display=swap" rel="stylesheet">
<style>
  :root{
    --brand-red:#ec2229;
    --ink:#111111;
    --paper:#ffffff;
    --stage:#e6e6e6;
    --text:#1c1c1c;
  }
  *{box-sizing:border-box;margin:0;padding:0}
  html,body{width:1200px;height:900px;overflow:hidden}
  body{
    background:radial-gradient(circle at 50% 45%,#f7f7f7 0%,var(--stage) 75%);
    font-family:"Montserrat",sans-serif;
    color:var(--text);
    position:relative;
  }
  .card{
    position:absolute;
    width:540px;height:310px;
    background:var(--paper);
    border-radius:16px;
    box-shadow:0 10px 28px rgba(0,0,0,.18);
    overflow:hidden;
  }
  .card--back{left:60px;top:130px}
  .card--front{left:600px;top:460px}

  /* back */
  .message-band{
    position:absolute;left:34px;right:34px;top:98px;height:114px;
    background:var(--ink);
    border-radius:14px;
    border-bottom:6px solid var(--brand-red);
    display:flex;align-items:center;justify-content:center;
  }
  .message{
    text-align:center;
    color:var(--paper);
    font-weight:800;
    font-variant:small-caps;
    font-size:21px;
    letter-spacing:.6px;
    line-height:1.4;
  }

  /* front */
  .tagline{
    position:absolute;top:24px;left:0;right:0;text-align:center;
    font-family:"Archivo Black",sans-serif;
    font-size:11px;letter-spacing:6px;color:var(--ink);
  }
  .brand{
    position:absolute;top:48px;left:0;right:0;
    display:flex;justify-content:center;align-items:center;gap:14px;
  }
  .brand__mark{width:18px;height:18px;background:var(--brand-red)}
  .brand__name{
    font-family:"Archivo Black",sans-serif;
    color:var(--ink);
    font-size:46px;line-height:1;text-align:center;letter-spacing:1px;
  }
  .brand__name span{display:block;font-size:21px;letter-spacing:9px;margin-top:8px}
  .address{
    position:absolute;right:34px;top:158px;width:250px;
    border-top:1.5px solid var(--brand-red);
    padding-top:10px;text-align:right;
    font-style:normal;
    font-size:13px;font-weight:500;line-height:1.5;
  }
  .contacts{
    position:absolute;left:34px;bottom:24px;width:280px;
    border-top:1.5px solid var(--brand-red);
    padding-top:10px;list-style:none;
    font-size:13.5px;font-weight:500;line-height:1.65;
  }
  .contacts li{display:flex;align-items:center;gap:8px}
  .contacts svg{width:14px;height:14px;flex:none}
</style>
</head>
<body>

<section class="card card--back" aria-label="Card back">
  <div class="message-band">
    <p class="message">"No more Tentants, No more Toilets"<br>"More Time, More Cash"</p>
  </div>
</section>

<section class="card card--front" aria-label="Card front">
  <p class="tagline">WE HELP PEOPLE LIVE!</p>
  <div class="brand">
    <span class="brand__mark"></span>
    <p class="brand__name">LAKEVIEW<span>NOTE BUYERS</span></p>
  </div>
  <address class="address">
    Lakeview Investors Group<br>
    P.O. Box 218<br>
    Millbrook, Kansas 67090
  </address>
  <ul class="contacts">
    <li>
      <svg viewBox="0 0 16 16" aria-hidden="true"><path fill="var(--brand-red)" d="M3.5 1.5l2.5 0 1 3.5-1.7 1.2a8 8 0 0 0 4.5 4.5L11 9l3.5 1v2.5c0 1-1 2-2 2A11 11 0 0 1 1.5 3.5c0-1 1-2 2-2z"/></svg>
      316-555-0148
    </li>
    <li>
      <svg viewBox="0 0 16 16" aria-hidden="true"><rect x="1" y="3" width="14" height="10" rx="1" fill="var(--brand-red)"/><path d="M1.5 3.8L8 9l6.5-5.2" fill="none" stroke="#fff" stroke-width="1.3"/></svg>
      info@lakeviewpaperfund.com
    </li>
    <li>
      <svg viewBox="0 0 16 16" aria-hidden="true"><circle cx="8" cy="8" r="7" fill="var(--brand-red)"/><path d="M1 8h14M8 1c-3 3.5-3 10.5 0 14M8 1c3 3.5 3 10.5 0 14" fill="none" stroke="#fff" stroke-width="1"/></svg>
      www.lakeviewpaperfund.com
    </li>
  </ul>
</section>

</body>
</html>
```